Verindo Living- Hang tags for Modern Handmade Home Decor products

We need to design some hang tags to use for our products, we want double tags, meaning two tags that go together on one string, two different and coordinating sizes and shapes. We have a logo, what we need is the artwork for these two tags to take to print. One tag will have the logo on one side and company information on the other, the second tag will be for product information. For example, we specialize in handmade pieces from Latin America, on the product tag I want space to write the product info but also a line for what country it's from and what community created it. I'm attaching an image of the shapes of tags that I like, along with a copy of our logo. On the larger company tag I'd like our logo in the center and a color block stripe of the yellow color of our logo at the bottom, on the flip side there will just be text, sort of our company motto. On the narrower longer product info tag I'd like a small logo at the bottom end and space for product information to be written in by hand and on the flip side of this one lines for what country it's from, what community created it and care instructions, again, all information that we will write in by hand. Please let me know if you have questions.

Target Market(s)

Design savvy, house proud, well educated people who travel and appreciate art.

Font styles to use
Sans Serif

Requirements
Must have
• I want it to look graphic, sophisticated and modern. I want to be very legible and clean.
Nice to have
• Clarity, easy to read, and maybe a bit of whimsy or lightheartedness.
Should not have
• Nothing that feels "ethnic" or "crafty:, even though our products are handmade in Latin America they are contemporary and sophisticated, not stereotypical.

```html
<!DOCTYPE html>
<html lang="en">
<head>
<meta charset="utf-8">
<title>Verindo Living – Hang Tags</title>
<link rel="stylesheet" href="https://fonts.googleapis.com/css2?family=Quicksand:wght@400;500&family=Kalam:wght@700&display=swap">
<style>
  :root {
    --paper: #ffffff;
    --kraft: #d4ae7c;
    --sun: #fccb0e;
    --slot: #2e2519;
    --ink: #131514;
    --mist: #b5c0c8;
    --chalk: #ffffff;
  }
  html, body {
    margin: 0;
    padding: 0;
    width: 1200px;
    height: 1059px;
    overflow: hidden;
    background: var(--paper);
  }
  .tag-set {
    display: block;
    width: 1200px;
    height: 1059px;
  }
  .brand-name {
    font-family: "Quicksand", sans-serif;
    font-weight: 400;
    font-size: 38px;
    fill: var(--mist);
  }
  .brand-web {
    font-family: "Quicksand", sans-serif;
    font-weight: 500;
    font-size: 10.5px;
    letter-spacing: 3px;
    fill: var(--mist);
  }
  .field-label {
    font-family: "Kalam", sans-serif;
    font-weight: 700;
    font-size: 20px;
    fill: var(--chalk);
  }
  .write-line {
    stroke: var(--chalk);
    stroke-width: 2.2;
  }
  .brand-small {
    font-family: "Quicksand", sans-serif;
    font-weight: 500;
    font-size: 17px;
    fill: var(--sun);
  }
</style>
</head>
<body>
<svg class="tag-set" viewBox="0 0 1200 1059" xmlns="http://www.w3.org/2000/svg" role="img" aria-label="Verindo Living hang tags: company tag and product information tag">

  <!-- Company tag -->
  <g class="company-tag">
    <polygon class="company-tag__body" points="266,333 302,297 548,297 584,333 584,760 266,760" fill="var(--kraft)"/>
    <rect class="company-tag__stripe" x="266" y="721" width="318" height="39" fill="var(--sun)"/>
    <path class="company-tag__slot" d="M405,297 H445 V349 Q445,357 437,357 H413 Q405,357 405,349 Z" fill="var(--slot)"/>
    <rect class="company-tag__slot-hole" x="416" y="308" width="18" height="31" fill="var(--paper)"/>
    <rect class="company-tag__brand-square" x="400" y="455" width="50" height="50" fill="var(--sun)"/>
    <text class="brand-name" x="425" y="590" text-anchor="middle">Verindo Living</text>
    <text class="brand-web" x="425" y="615" text-anchor="middle">www.verindoliving.com</text>
  </g>

  <!-- Product information tag -->
  <g class="product-tag">
    <polygon class="product-tag__body" points="628,200 704,149 859,149 934,200 934,908 628,908" fill="var(--ink)"/>
    <circle class="product-tag__hole" cx="781" cy="206" r="14" fill="var(--paper)"/>

    <text class="field-label" x="648" y="297">Created by</text>
    <text class="field-label" x="751" y="299">:</text>
    <line class="write-line" x1="766" y1="298" x2="914" y2="298"/>

    <text class="field-label" x="648" y="344">Country</text>
    <text class="field-label" x="751" y="346">:</text>
    <line class="write-line" x1="766" y1="345" x2="914" y2="345"/>

    <g class="product-tag__notes">
      <line class="write-line" x1="648" y1="407" x2="914" y2="407"/>
      <line class="write-line" x1="648" y1="453" x2="914" y2="453"/>
      <line class="write-line" x1="648" y1="499" x2="914" y2="499"/>
      <line class="write-line" x1="648" y1="545" x2="914" y2="545"/>
      <line class="write-line" x1="648" y1="591" x2="914" y2="591"/>
      <line class="write-line" x1="648" y1="637" x2="914" y2="637"/>
      <line class="write-line" x1="648" y1="683" x2="914" y2="683"/>
      <line class="write-line" x1="648" y1="729" x2="914" y2="729"/>
      <line class="write-line" x1="648" y1="775" x2="914" y2="775"/>
    </g>

    <text class="brand-small" x="781" y="858" text-anchor="middle">Verindo Living</text>
  </g>
</svg>
</body>
</html>
```